2024 Valcor Drayman mid roof Vehicle wrap design for a NYC based HVAC company

We have a 2024 Valcor Drayman Mid Roof that needs a vehicle wrap design for our business. We are a heating and air conditioning company in New York City that does residential and commercial work. We service and install high-end, luxury homes, apartments, offices and stores. Our colors are blue and orange. The vehicle is white. We want the design to be clean, modern and minimal. Nothing cartoony. Please avoid flames and snowflakes, everyone uses them and we're trying to stand out. We are required to have our company name and phone number on both sides of the vehicle in a minimum 3" font. Attached are files of our logo
Target Market(s)
High-end luxury homes, stores and offices in NYC
Industry/Entity Type
Heating and Air Conditioning
Other font styles liked:
- anything with a rounded look I think
Requirements
Must have
- 3" letters with address and phone number on both sides. Would also like a QR code on the back of the vehicle to our website. Also include the website address on the sides with the phone and address. Should be a clean and quiet design but eye catching
Nice to have
- Minimal look but still take advantage of a wrap instead of traditional boring vinyl lettering. It may be nice to say "Residential and Commercial" and/or "Heating and Air Conditioning" on the vehicle somewhere if it fits within the design.
Should not have
- No snowflakes, no flames, no typical air conditioning and heating icons. Nothing cartoon looking.

```html
<!DOCTYPE html>
<html lang="en">
<head>
<meta charset="utf-8">
<title>BrightAir Mechanical Inc. – Van Side Wrap</title>
<link rel="stylesheet" href="https://fonts.googleapis.com/css2?family=Open+Sans:wght@600;700&display=swap">
<style>
  :root {
    --wrap-white: #f7f7f7;
    --canvas-bg: #e6e7e8;
    --brand-orange: #d4512c;
    --brand-rust: #a8503a;
    --brand-slate: #5d6a78;
    --brand-blue: #2e8fc4;
    --brand-blue-deep: #2a7db0;
    --ring-teal: #2a9bc0;
    --text-light: #ffffff;
  }
  * { margin: 0; padding: 0; box-sizing: border-box; }
  html, body {
    width: 1200px;
    height: 566px;
    overflow: hidden;
    background: var(--canvas-bg);
  }
  .wrap-side {
    position: relative;
    width: 1200px;
    height: 566px;
    background: var(--wrap-white);
    font-family: "Open Sans", Arial, sans-serif;
  }
  .brand-band {
    position: absolute;
    left: 620px;
    top: 132px;
    width: 580px;
    height: 222px;
    background: linear-gradient(180deg,
      var(--brand-orange) 0%,
      var(--brand-rust) 28%,
      var(--brand-slate) 52%,
      var(--brand-blue-deep) 76%,
      var(--brand-blue) 100%);
  }
  .brand-disc {
    position: absolute;
    left: 490px;
    top: 126px;
    width: 232px;
    height: 232px;
    border-radius: 50%;
    background: var(--wrap-white);
  }
  .brand-mark-area {
    position: absolute;
    left: 516px;
    top: 152px;
    width: 180px;
    height: 180px;
    border-radius: 50%;
    background: linear-gradient(180deg, #c4694e 0%, #8a7a80 50%, #3f8fbd 100%);
    opacity: 0.85;
  }
  .company-name {
    position: absolute;
    left: 736px;
    top: 160px;
    color: var(--text-light);
    font-weight: 700;
    line-height: 1;
  }
  .company-name .name-main {
    display: block;
    font-size: 60px;
    letter-spacing: -1px;
  }
  .company-name .name-sub {
    display: block;
    margin-top: 8px;
    padding-left: 32px;
    font-size: 22px;
    letter-spacing: 9px;
  }
  .contact {
    position: absolute;
    left: 752px;
    top: 272px;
    width: 310px;
    color: var(--text-light);
    font-weight: 600;
    text-align: center;
  }
  .contact .web {
    font-size: 19px;
    letter-spacing: 0.3px;
  }
  .contact .phone {
    margin-top: 10px;
    font-size: 21px;
    display: flex;
    align-items: center;
    justify-content: center;
    gap: 6px;
  }
  .contact .phone svg { width: 22px; height: 22px; }
  .service-line {
    position: absolute;
    left: 189px;
    top: 326px;
    color: var(--brand-blue);
    font-weight: 700;
    font-size: 20px;
    letter-spacing: 0.2px;
    transform: rotate(-1.5deg);
    transform-origin: left center;
  }
</style>
</head>
<body>
  <main class="wrap-side">
    <div class="brand-band"></div>
    <div class="brand-disc"></div>
    <div class="brand-mark-area" role="img" aria-label="Company brand mark area"></div>

    <h1 class="company-name">
      <span class="name-main">BrightAir</span>
      <span class="name-sub">MECHANICAL INC.</span>
    </h1>

    <div class="contact">
      <p class="web">www.brightairmechanical.com</p>
      <p class="phone">
        <svg viewBox="0 0 24 24" aria-hidden="true">
          <circle cx="12" cy="12" r="10.5" fill="none" stroke="#fff" stroke-width="1.8"/>
          <path d="M8.6 6.8c.4-.3 1-.2 1.2.3l.9 1.9c.2.4.1.8-.2 1.1l-.7.6c.5 1.2 1.4 2.2 2.6 2.8l.6-.7c.3-.3.7-.4 1.1-.2l1.9.9c.5.2.6.8.3 1.2l-.8 1c-.5.6-1.300.8-2 .5-2.7-1.1-4.8-3.2-5.8-5.9-.3-.7-.1-1.5.5-2z" fill="#fff"/>
        </svg>
        (555) 014-2290
      </p>
    </div>

    <p class="service-line">HEATING AND AIR CONDITIONING</p>
  </main>
</body>
</html>
```